Midnight Lantern Diva

We have started working on a website for our short film. The goals of this website are:
• Attract talent, financiers + distributors to the feature film.
• Start e-commerce business to generate buzz for the film.

Who is our target audience?
• Kung Fu fans.
• Guitar players.
• Women filmmakers.
• Chinese film fans.

Information we want on this website.
Web 1.0 Components
• Media - trailer and stills

We are looking to include the following pages:
1. Home page
2. About
3. Photos
4. Cast & Crew
5. News
6. Media (reviews)
7. Store
8. Contact

Web 2.0 Components
• Mailing list sign-up
• Blog - with comments section
• Like / Add buttons - to all social networks
• Feeds - from social media
• Links - social media
• Widgets - that anyone can put on their sites

Attached is a mock up of the landing page (possible T-shirt) we are developing plus photos we would like on the website.

Thank you.
Updates

Reason: I am at a film market in meetings for my film project. Next week will be used for script rewrites. After that I will choose a design.

Hello Folks,

I have added my company logo to my brief. My answer is yes - I would like that added to the website.
Thanks!
M-

Reason: I have added more photos and included two (in front of a white screen) that can easily be photoshopped into a great landing page. M-

I have added more photos. Also I have two photos taken in front of a white screen that can easily be photo-shopped into a cool landing page. I have also gotten rid of the "crowd" photo in my mock up of the design I am looking for. 

I've extended the deadline by 2 days.

M-

Target Market(s)

• Kung Fu fans.
• Guitar players.
• Women filmmakers.
• Chinese film fans.

Industry/Entity Type

E-Commerce

Colors
ec2027

Requirements
Must have
• Trailer, movie stills, links to social media.
Nice to have
• All of the above

```html
<!DOCTYPE html>
<html lang="en">
<head>
<meta charset="utf-8">
<title>Midnight Lantern Diva</title>
<link rel="stylesheet" href="https://fonts.googleapis.com/css2?family=Macondo&family=PT+Sans:wght@400;700&display=swap">
<style>
  :root {
    --red: #ec2027;
    --red-deep: #8e0f14;
    --black: #000000;
    --ink: #0b0b0b;
    --white: #ffffff;
    --grey: #b9b9b9;
    --amber: #b8650a;
    --tweet-band: #2a1f20;
    --heading: "Macondo", fantasy;
    --body: "PT Sans", sans-serif;
  }
  * { box-sizing: border-box; margin: 0; padding: 0; }
  html, body { width: 896px; height: 1200px; overflow: hidden; background: var(--black); }
  body { font-family: var(--body); color: var(--white); }
  .page { position: relative; width: 896px; height: 1200px; background: var(--black); }
  .abs { position: absolute; }

  .main-nav { left: 0; top: 0; width: 896px; height: 38px; background: var(--red); }
  .main-nav ul { list-style: none; position: absolute; right: 58px; top: 0; display: flex; height: 38px; }
  .main-nav li { height: 38px; line-height: 38px; padding: 0 15px; font-size: 14px; }
  .main-nav li.current { background: var(--ink); }

  .hero { left: 0; top: 38px; width: 896px; height: 244px;
    background:
      linear-gradient(180deg, rgba(0,0,0,0.55) 0%, rgba(0,0,0,0) 30%, rgba(0,0,0,0) 75%, rgba(0,0,0,0.85) 100%),
      linear-gradient(90deg, #000 0%, #0d0604 18%, #3a1606 30%, #8a3a0c 40%, #c65218 48%, #d94aa8 58%, #e0327a 64%, #c8321a 72%, #7a1c08 84%, #1e0804 95%, #000 100%); }
  .hero-title { left: 80px; top: 82px; width: 200px; font-weight: 700; color: var(--white); font-size: 32px; line-height: 34px; }

  .intro { left: 66px; top: 281px; width: 759px; height: 216px;
    background: linear-gradient(180deg, var(--red) 0%, #c4161d 40%, #5a0a0d 78%, #0a0202 100%); }
  .trailer { left: 21px; top: 15px; width: 277px; height: 184px;
    background:
      linear-gradient(90deg, rgba(0,0,0,0.55) 0%, rgba(0,0,0,0) 35%, rgba(0,0,0,0) 65%, rgba(0,0,0,0.6) 100%),
      linear-gradient(180deg, #9c9588 0%, #6a6257 30%, #3c3630 65%, #1c1916 100%); }
  .trailer svg { position: absolute; left: 77px; top: 20px; }
  .trailer .label { position: absolute; left: 0; right: 0; bottom: 12px; text-align: center; letter-spacing: 5px; font-size: 19px; color: #c9c2b5; }
  .intro h1 { position: absolute; left: 334px; top: 24px; font-family: var(--heading); font-weight: 400; font-size: 29px; color: #1a0204; white-space: nowrap; }
  .intro p { position: absolute; left: 335px; top: 69px; width: 390px; font-size: 15.5px; line-height: 18px; }
  .btn-dark { position: absolute; left: 597px; top: 175px; width: 149px; height: 25px; background: var(--ink); font-size: 12.5px; line-height: 25px; text-align: center; }

  .band { left: 0; top: 497px; width: 896px; height: 54px;
    background:
      linear-gradient(90deg, #000 0%, rgba(0,0,0,0) 12%, rgba(0,0,0,0) 88%, #000 100%),
      linear-gradient(180deg, #5a3c06 0%, #7a6412 35%, #5a4a0a 65%, #0a0800 100%); }

  h2 { position: absolute; font-family: var(--heading); font-weight: 400; font-size: 33px; color: var(--white); }
  .arrow { position: absolute; width: 20px; height: 21px; background: var(--red); }
  .arrow svg { display: block; }

  .gallery-frame { left: 69px; top: 616px; width: 377px; height: 193px; background: var(--red); }
  .gallery-photo { position: absolute; left: 11px; top: 12px; width: 355px; height: 168px; border: 1px solid var(--white);
    background:
      linear-gradient(180deg, rgba(0,0,0,0.35) 0%, rgba(0,0,0,0) 40%, rgba(90,10,14,0.45) 100%),
      linear-gradient(90deg, #120808 0%, #3a1a16 15%, #8a6050 30%, #a87a62 38%, #6a2a26 52%, #3a1216 70%, #1a0a0c 100%); }

  .news-item { position: absolute; left: 495px; width: 340px; }
  .news-thumb { position: absolute; left: 0; top: 0; width: 121px; height: 98px; background: var(--red); }
  .news-thumb div { position: absolute; left: 10px; top: 10px; width: 102px; height: 77px; border: 1px solid var(--white); }
  .news-item p { position: absolute; left: 136px; top: 2px; width: 205px; font-size: 13.5px; line-height: 16px; }
  .read-more { position: absolute; font-size: 12.5px; }

  .crew-thumb { left: 66px; top: 891px; width: 91px; height: 81px;
    background: linear-gradient(90deg, #6a2a22 0%, #a86048 40%, #8a3a2c 60%, #4a1a14 100%); }
  .crew-text { left: 177px; top: 890px; font-size: 13.5px; line-height: 16px; }

  .newsletter { left: 493px; top: 887px; width: 332px; height: 102px; background: var(--amber); }
  .newsletter h3 { position: absolute; left: 22px; top: 10px; font-family: var(--heading); font-weight: 400; font-size: 30px; }
  .newsletter .field { position: absolute; left: 20px; top: 56px; width: 202px; height: 30px; background: var(--black); }
  .newsletter .subscribe { position: absolute; left: 228px; top: 56px; width: 94px; height: 30px; background: var(--red); font-size: 14px; line-height: 30px; text-align: center; }

  .tweets { left: 0; top: 1019px; width: 896px; height: 67px; background: var(--tweet-band); }
  .tweets .feed-icon { position: absolute; left: 80px; top: 15px; }
  .tweets p { position: absolute; left: 138px; top: 24px; font-size: 13.5px; }

  .footer-nav { left: 0; top: 1087px; width: 896px; height: 34px; background: var(--red); }
  .footer-nav ul { list-style: none; position: absolute; left: 148px; top: 0; display: flex; }
  .footer-nav li { line-height: 34px; padding: 0 15px; font-size: 14px; color: #f4c3c4; }

  .footer-title { left: 116px; top: 1133px; width: 130px; font-weight: 700; font-size: 16px; line-height: 18px; color: var(--white); }
  .legal { left: 256px; top: 1136px; font-size: 13px; line-height: 23px; color: var(--grey); }
  .social { left: 564px; top: 1142px; display: flex; gap: 4px; }
  .social span { width: 28px; height: 28px; border-radius: 50%; background: var(--red); display: flex; align-items: center; justify-content: center; }
</style>
</head>
<body>
<div class="page">

  <nav class="main-nav abs">
    <ul>
      <li class="current">Home</li><li>About</li><li>Photos</li><li>Cast &amp; Crew</li><li>News</li><li>Media</li><li>Store</li><li>Contact</li>
    </ul>
  </nav>

  <div class="hero abs" role="img" aria-label="Hero artwork: a performer in a flying kick over a burst of pink and orange stage light with a crowd silhouette and a guitar"></div>
  <div class="hero-title abs">Midnight Lantern Diva</div>

  <section class="intro abs">
    <div class="trailer abs" role="img" aria-label="Trailer still: a silhouetted figure in a misty, lamp-lit corridor">
      <svg width="102" height="102" viewBox="0 0 102 102">
        <circle cx="51" cy="51" r="47" fill="none" stroke="#ffffff" stroke-width="5"/>
        <path d="M42 36 L66 51 L42 66 Z" fill="#ffffff"/>
      </svg>
      <span class="label">TRAILER</span>
    </div>
    <h1>Which the midnight lantern diva</h1>
    <p>Your best resource for everything related to the most explosive and dynamic rising star of action cinema. With exclusive news, videos, galleries and fitness advice from the man himself, make sure you sign up to our newsletter. Enjoy the site and come back soon.</p>
    <span class="btn-dark">Read more about us</span>
  </section>

  <div class="band abs" role="img" aria-label="Decorative band of golden swirling lines"></div>

  <h2 style="left:81px;top:557px;">Photo Gallery</h2>
  <span class="arrow" style="left:381px;top:572px;"><svg width="20" height="21"><path d="M12 5 L7 10.5 L12 16" fill="none" stroke="#fff" stroke-width="1.8"/></svg></span>
  <span class="arrow" style="left:410px;top:572px;"><svg width="20" height="21"><path d="M8 5 L13 10.5 L8 16" fill="none" stroke="#fff" stroke-width="1.8"/></svg></span>
  <div class="gallery-frame abs">
    <div class="gallery-photo" role="img" aria-label="Film still: the lead actress in a red jacket in a dim club"></div>
  </div>

  <h2 style="left:497px;top:562px;">Latest News Post</h2>
  <article class="news-item" style="top:616px;">
    <div class="news-thumb"><div role="img" aria-label="News photo: the actress in a warm-lit scene" style="background:linear-gradient(90deg,#5a2a22 0%,#a86a55 35%,#6a4a40 60%,#8a8480 100%);"></div></div>
    <p>Your best resource for everything related to the most explosive and dynamic rising star of action cinema.</p>
    <span class="read-more" style="left:138px;top:85px;">Read more</span>
  </article>
  <article class="news-item" style="top:745px;">
    <div class="news-thumb"><div role="img" aria-label="News photo: the actress singing with a guitar" style="background:linear-gradient(180deg,#3a2a26 0%,#7a4a3a 45%,#8a3a2c 70%,#3a1a14 100%);"></div></div>
    <p>Your best resource for everything related to the most explosive and dynamic rising star of action cinema.</p>
    <span class="read-more" style="left:138px;top:83px;">Read more</span>
  </article>

  <h2 style="left:81px;top:827px;">Cast &amp; Crew</h2>
  <div class="crew-thumb abs" role="img" aria-label="Photo: the actress playing guitar on stage"></div>
  <div class="crew-text abs">Directors: Harlan Voss<br>Producer: Dorian Pell<br>Writer: Tessa Marlow</div>
  <span class="read-more abs" style="left:177px;top:957px;">Read more</span>

  <section class="newsletter abs">
    <h3>Email Newsletter</h3>
    <div class="field"></div>
    <span class="subscribe">Subscribe</span>
  </section>

  <section class="tweets abs">
    <svg class="feed-icon" width="40" height="38" viewBox="0 0 40 38" role="img" aria-label="Feed icon">
      <path d="M6 4 H34 A4 4 0 0 1 38 8 V24 A4 4 0 0 1 34 28 H16 L8 35 V28 H6 A4 4 0 0 1 2 24 V8 A4 4 0 0 1 6 4 Z" fill="#ffffff"/>
      <circle cx="12" cy="16" r="2.4" fill="#2a1f20"/><circle cx="20" cy="16" r="2.4" fill="#2a1f20"/><circle cx="28" cy="16" r="2.4" fill="#2a1f20"/>
    </svg>
    <p>@Discover who Rex Calder is and why so many “big names” listen to him, and how BrightLane Promotions ...</p>
    <span class="arrow" style="left:767px;top:0;"><svg width="20" height="21"><path d="M12 5 L7 10.5 L12 16" fill="none" stroke="#fff" stroke-width="1.8"/></svg></span>
    <span class="arrow" style="left:797px;top:0;"><svg width="20" height="21"><path d="M8 5 L13 10.5 L8 16" fill="none" stroke="#fff" stroke-width="1.8"/></svg></span>
  </section>

  <nav class="footer-nav abs">
    <ul><li>Home</li><li>About</li><li>Photos</li><li>Cast &amp; Crew</li><li>News</li><li>Media</li><li>Store</li><li>Contact</li></ul>
  </nav>

  <div class="footer-title abs">Midnight<br>Lantern Diva</div>
  <div class="legal abs">Copyright &copy; 2014<br>Privacy Policy &nbsp;|&nbsp; Legal Notices</div>
  <div class="social abs" aria-label="Social links">
    <span><svg width="16" height="16" viewBox="0 0 16 16"><path d="M2 3 H14 V11 H7 L4 14 V11 H2 Z" fill="none" stroke="#fff" stroke-width="1.6" stroke-linejoin="round"/></svg></span>
    <span><svg width="16" height="16" viewBox="0 0 16 16"><circle cx="4" cy="8" r="2" fill="#fff"/><circle cx="12" cy="3.5" r="2" fill="#fff"/><circle cx="12" cy="12.5" r="2" fill="#fff"/><path d="M4 8 L12 3.5 M4 8 L12 12.5" stroke="#fff" stroke-width="1.4"/></svg></span>
    <span><svg width="16" height="16" viewBox="0 0 16 16"><path d="M7 9 L9 7 M6 6 L4 8 A2.5 2.5 0 0 0 8 12 L10 10 M10 10 M10 6 L12 4 A2.5 2.5 0 0 0 8 0.5" fill="none" stroke="#fff" stroke-width="1.6" stroke-linecap="round"/></svg></span>
    <span><svg width="16" height="16" viewBox="0 0 16 16"><rect x="1.5" y="4.5" width="13" height="9" rx="1.5" fill="none" stroke="#fff" stroke-width="1.5"/><circle cx="8" cy="9" r="2.4" fill="none" stroke="#fff" stroke-width="1.5"/><rect x="5" y="2.5" width="6" height="2" fill="#fff"/></svg></span>
    <span><svg width="16" height="16" viewBox="0 0 16 16"><path d="M8 3 V13 M3 8 H13" stroke="#fff" stroke-width="2" stroke-linecap="round"/></svg></span>
    <span><svg width="16" height="16" viewBox="0 0 16 16"><rect x="1.5" y="3.5" width="13" height="9" rx="1" fill="none" stroke="#fff" stroke-width="1.5"/><path d="M2 4 L8 9 L14 4" fill="none" stroke="#fff" stroke-width="1.5"/></svg></span>
  </div>

</div>
</body>
</html>
```